Business Card Design for Flood Rescue 360 - Property Restoration Professionals

I need a business card designed for Flood Rescue 360. We are a full-service property restoration solution. Providing water, fire, smoke & storm restoration as well as mold remediation and full remodel or reconstruction to homes and businesses across Dallas-Fort Worth, TX.
Target Market(s)
home and business owners with insurance covered property damage from water, fire or storm related damage
Industry/Entity Type
property restoration
Contact Information for Business Card
Martin Kell General Manager Cell: 214-555-0193 Office: 469-555-0148 email: Martin@FloodRescue360.example services: Water, Fire, Mold, Reconstruction Tagline: Urgency for Your Water Emergency!
Look and feel
Each slider illustrates characteristics of the customer's brand and the style your logo design should communicate.

```html
<!DOCTYPE html>
<html lang="en">
<head>
<meta charset="utf-8">
<title>Flood Rescue 360 – Business Card</title>
<link rel="stylesheet" href="https://fonts.googleapis.com/css2?family=Roboto:wght@400;500;900&display=swap">
<style>
  :root {
    --brand-blue: #16b1e6;
    --ink: #1c1c1c;
    --slate: #7a7a7a;
    --paper: #ffffff;
    --backdrop: #d3d6d6;
  }
  * { margin: 0; padding: 0; box-sizing: border-box; }
  html, body { width: 1200px; height: 960px; overflow: hidden; }
  body {
    background: var(--backdrop);
    font-family: "Roboto", Arial, sans-serif;
    color: var(--ink);
    position: relative;
  }
  .card {
    position: absolute;
    left: 250px;
    width: 700px;
    height: 400px;
    background: var(--paper);
    border-left: 4px solid var(--brand-blue);
    border-bottom: 3px solid var(--brand-blue);
  }
  .card--front { top: 60px; }
  .card--back { top: 500px; }

  .wordmark {
    font-weight: 900;
    color: var(--brand-blue);
    text-transform: uppercase;
    line-height: 0.95;
    letter-spacing: -1px;
    position: absolute;
  }
  .card--front .wordmark {
    left: 0; right: 0;
    top: 112px;
    text-align: center;
    font-size: 76px;
  }

  .services {
    position: absolute;
    left: 0; right: 0;
    top: 330px;
    text-align: center;
  }
  .services__heading {
    display: flex;
    align-items: center;
    justify-content: center;
    gap: 8px;
    color: var(--brand-blue);
    font-size: 17px;
    font-weight: 500;
  }
  .services__rule {
    width: 122px;
    height: 2px;
    background: linear-gradient(90deg, rgba(22,177,230,0.2), var(--brand-blue), rgba(22,177,230,0.2));
  }
  .services__list {
    margin-top: 6px;
    display: flex;
    justify-content: center;
    gap: 7px;
    font-size: 18px;
    list-style: none;
  }
  .services__list li { display: flex; align-items: center; gap: 6px; }
  .services__dot {
    width: 11px; height: 11px;
    border-radius: 50%;
    border: 2px solid var(--brand-blue);
  }

  .card--back .wordmark {
    left: 24px;
    top: 157px;
    font-size: 46px;
  }
  .divider {
    position: absolute;
    left: 345px;
    top: 80px;
    width: 1px;
    height: 242px;
    background: var(--brand-blue);
  }
  .contact {
    position: absolute;
    left: 379px;
    top: 124px;
  }
  .contact__name {
    font-size: 36px;
    font-weight: 500;
    line-height: 1;
  }
  .contact__first { color: var(--brand-blue); }
  .contact__last { color: var(--slate); font-weight: 400; }
  .contact__role { font-size: 17px; margin-top: 4px; }
  .contact__lines { list-style: none; margin-top: 26px; }
  .contact__lines li {
    display: flex;
    align-items: center;
    gap: 10px;
    font-size: 17px;
    letter-spacing: 0.6px;
    height: 23.5px;
  }
  .contact__icon { width: 15px; height: 15px; flex: none; }
  .tagline {
    position: absolute;
    left: 0; right: 0;
    top: 352px;
    text-align: center;
    color: var(--brand-blue);
    font-size: 18px;
    letter-spacing: 0.3px;
  }
</style>
</head>
<body>
  <section class="card card--front">
    <div class="wordmark">Flood<br>Rescue 360</div>
    <div class="services">
      <div class="services__heading">
        <span class="services__rule"></span>SERVICES<span class="services__rule"></span>
      </div>
      <ul class="services__list">
        <li><span class="services__dot"></span>Water</li>
        <li><span class="services__dot"></span>Fire</li>
        <li><span class="services__dot"></span>Mold</li>
        <li><span class="services__dot"></span>Reconstruction</li>
      </ul>
    </div>
  </section>

  <section class="card card--back">
    <div class="wordmark">Flood<br>Rescue 360</div>
    <div class="divider"></div>
    <div class="contact">
      <p class="contact__name"><span class="contact__first">Martin</span> <span class="contact__last">Kell</span></p>
      <p class="contact__role">General Manager</p>
      <ul class="contact__lines">
        <li>
          <svg class="contact__icon" viewBox="0 0 16 16" aria-hidden="true"><rect x="4" y="1" width="8" height="14" rx="1.5" fill="none" stroke="#16b1e6" stroke-width="1.6"/></svg>
          214-555-0193
        </li>
        <li>
          <svg class="contact__icon" viewBox="0 0 16 16" aria-hidden="true"><path d="M3 2l3 0 1 3-2 1.5c1 2 2.5 3.5 4.5 4.5L11 9l3 1v3c0 .6-.4 1-1 1C7 14 2 9 2 3c0-.6.4-1 1-1z" fill="#16b1e6"/></svg>
          469-555-0148
        </li>
        <li>
          <svg class="contact__icon" viewBox="0 0 16 16" aria-hidden="true"><rect x="1" y="4" width="14" height="10" fill="#16b1e6"/><path d="M1 4l7 5 7-5" fill="none" stroke="#fff" stroke-width="1.2"/></svg>
          Martin@FloodRescue360.example
        </li>
      </ul>
    </div>
    <p class="tagline">Urgency for Your Water Emergency!</p>
  </section>
</body>
</html>
```